Velanqua Cookbook (Independant Velanqua Consultant - not Velanqua themselves)

Approx 120 page Recipe book, need design created for recipe pages.
each recipe illustrated with full colour photograph (supplied) on opposite page.
To included index, contents page, intro, etc
Cover design also to be suggested.
We must have a professional finish, but with a friendly, family theme.
Reason: Deadline extended because I require further designs, please.

```html
<!DOCTYPE html>
<html lang="en">
<head>
<meta charset="utf-8">
<title>Dreamy Raspberry Delight – Recipe Spread</title>
<link rel="stylesheet" href="https://fonts.googleapis.com/css2?family=Kaushan+Script&family=Cormorant+SC:wght@500;700&family=Cormorant+Garamond:ital,wght@1,700&display=swap">
<style>
  :root {
    --paper: #ffffff;
    --rose: #ad6469;
    --rose-title: #a9585e;
    --cream: #f3e7d6;
    --dot: #dccdb4;
    --ink: #1d1a1a;
    --badge-tan: #b89a7a;
    --badge-green: #8fa86c;
    --badge-rose: #b0656c;
    --photo-light: #d9dadd;
    --photo-mid: #cfc9c8;
    --photo-berry: #c86a80;
  }
  * { margin: 0; padding: 0; box-sizing: border-box; }
  html, body { width: 1200px; height: 600px; overflow: hidden; background: var(--paper); }
  .spread { position: relative; width: 1200px; height: 600px; }

  .recipe-page { position: absolute; left: 0; top: 0; width: 441px; height: 600px; background: var(--paper); }
  .recipe-title {
    position: absolute; left: 30px; top: 24px;
    font-family: "Kaushan Script", cursive; font-size: 21px; letter-spacing: 1px;
    color: var(--rose-title); text-transform: uppercase; font-weight: 400;
    transform: skewX(-6deg);
  }
  .column { position: absolute; text-align: center; color: var(--ink); }
  .ingredients { left: 40px; width: 164px; top: 188px; }
  .instructions { left: 252px; width: 178px; top: 188px; }
  .column-heading {
    font-family: "Cormorant SC", serif; font-weight: 700; font-size: 15px;
    letter-spacing: 0.3px; margin-bottom: 6px;
  }
  .ingredient-list { list-style: none; }
  .ingredient-list li {
    font-family: "Cormorant Garamond", serif; font-style: italic; font-weight: 700;
    font-variant: small-caps; font-size: 12.5px; line-height: 15.2px;
  }
  .method p {
    font-family: "Cormorant SC", serif; font-weight: 500; font-size: 13px; line-height: 15.2px;
  }
  .divider { position: absolute; left: 212px; top: 113px; }

  .diet-badges { position: absolute; left: 179px; top: 492px; display: flex; gap: 4px; }
  .badge {
    width: 21px; height: 21px; border-radius: 50%;
    font-family: "Cormorant SC", serif; font-size: 10px; color: var(--cream);
    display: flex; align-items: center; justify-content: center;
  }
  .badge--df { background: var(--badge-tan); }
  .badge--gf { background: var(--badge-green); }
  .badge--ef { background: var(--badge-rose); }

  .tagline-band {
    position: absolute; left: 0; top: 541px; width: 441px; height: 50px;
    background: var(--rose); display: flex; align-items: center; justify-content: center;
  }
  .tagline { font-family: "Kaushan Script", cursive; font-size: 17px; color: var(--cream); }

  .photo-page {
    position: absolute; left: 441px; top: 0; width: 759px; height: 600px;
    background:
      radial-gradient(ellipse 230px 260px at 420px 300px, var(--photo-berry) 0%, #d98fa0 55%, rgba(217,143,160,0) 100%),
      linear-gradient(90deg, var(--photo-light), var(--photo-mid) 60%, var(--photo-light));
  }
  .photo-veil { position: absolute; left: 441px; top: 0; width: 159px; height: 600px; background: rgba(255,255,255,0.35); }
</style>
</head>
<body>
<main class="spread">
  <section class="recipe-page">
    <h1 class="recipe-title">Dreamy Raspberry Delight</h1>

    <div class="column ingredients">
      <h2 class="column-heading">Ingredients</h2>
      <ul class="ingredient-list">
        <li>400g frozen raspberries</li>
        <li>1 tin sweetened condensed milk</li>
        <li>130g cream</li>
        <li>30g lemon juice</li>
        <li>30g sugar</li>
      </ul>
    </div>

    <svg class="divider" width="8" height="270" viewBox="0 0 8 270" aria-hidden="true">
      <g fill="var(--dot)">
        <circle cx="4" cy="4" r="3.2"/><circle cx="4" cy="22.6" r="3.2"/><circle cx="4" cy="41.2" r="3.2"/>
        <circle cx="4" cy="59.8" r="3.2"/><circle cx="4" cy="78.4" r="3.2"/><circle cx="4" cy="97" r="3.2"/>
        <circle cx="4" cy="115.6" r="3.2"/><circle cx="4" cy="134.2" r="3.2"/><circle cx="4" cy="152.8" r="3.2"/>
        <circle cx="4" cy="171.4" r="3.2"/><circle cx="4" cy="190" r="3.2"/><circle cx="4" cy="208.6" r="3.2"/>
        <circle cx="4" cy="227.2" r="3.2"/><circle cx="4" cy="245.8" r="3.2"/><circle cx="4" cy="264.4" r="3.2"/>
      </g>
    </svg>

    <div class="column instructions">
      <h2 class="column-heading">Step-by-step Instructions</h2>
      <div class="method">
        <p>Place all ingredients in bowl.</p>
        <p>Mix for 1 minute on Speed 8 until smooth.</p>
        <p>Transfer to plastic container and freeze 4 hours or until solid.</p>
        <p>Soften slightly before serving.</p>
      </div>
    </div>

    <div class="diet-badges">
      <span class="badge badge--df">DF</span>
      <span class="badge badge--gf">GF</span>
      <span class="badge badge--ef">EF</span>
    </div>

    <div class="tagline-band">
      <p class="tagline">Another ice cream made in next to no time!</p>
    </div>
  </section>

  <div class="photo-page" role="img" aria-label="Photograph of raspberry ice cream scoops topped with frosted frozen raspberries in a glass sundae dish with a white straw"></div>
  <div class="photo-veil" aria-hidden="true"></div>
</main>
</body>
</html>
```